New Packaging and label for New Beard Oil and Shampoo brand from London

Oils, Shampoo ect .. Beard Oil Ingredients: Application Directions: Apply to beard by weight in a small amount of oil will naturally absorb. Leaving it soft & conditioned. Ingredients: Coconut oil, scented oil, Oud oil, vitamin E 100% Natural `i will have 5 types of oils Vanilla Oud Rose Oud Cocktail Tea tree Arabian Night

Target Market(s)

A fashionable well groomed professional gentleman who is willing to invest in his appearance.

Industry/Entity Type

It Company

Font styles to use
Sans Serif

Colors

Designer to choose colors to be used in the design.

Requirements
Must have
• Beard Oil Ingredients: Application Directions: Apply to a beard by a small amount of oil will naturally absorb. Leaving it soft & conditioned. Ingredients: Coconut Oil, Scented Oil, Oil Oud, Vitamin E 100% Natural 1.0z 30ml Made in Uk i will have 5 types of oils Vanilla Oud Rose Oud Cocktail Tea Tree Arabian Beard Night Shampoo APPLICATION DIRECTIONS Massage into the beard / hair and rinse out with warm water. Distorted shampoos, there are no nasty chemicals which are damaging your beard instead of the wheat proteins and oils that you add to the hair follicles with nutrients and naturally adding a protective coating. INGREDIENTS Aqua (Water), Capryl / caprylyl glucoside, Cocomidopropyl betaine, Glycerin (Veg), Xanthan gum, Phenoxyethanol, Hydrolysed wheat protein, Aloe barbadensis (Aloe vera) leaf powder, Sodium benzoate, Potassium sorbate1 3.4 oz, 100ml Cylinder packaging for the Oils, Box for the shampoo
Nice to have
• I want "London" written underneath the logo and oil name.

```html
<!DOCTYPE html>
<html lang="en">
<head>
<meta charset="utf-8">
<title>Tea Tree Beard Shampoo – Label</title>
<link rel="stylesheet" href="https://fonts.googleapis.com/css2?family=Josefin+Sans:wght@300;400;600;700&display=swap">
<style>
  :root {
    --page: #ffffff;
    --panel: #231f20;
    --gold: #c9a74f;
    --white: #ffffff;
    --grey: #b9b6b4;
  }
  * { margin: 0; padding: 0; box-sizing: border-box; }
  html, body {
    width: 1145px; height: 1200px; overflow: hidden;
    background: var(--page);
    font-family: "Josefin Sans", sans-serif;
  }
  .label {
    position: absolute; top: 47px;
    width: 489px; height: 1101px;
    background: var(--panel);
    color: var(--white);
    text-align: center;
  }
  .label--front { left: 52px; }
  .label--back { left: 604px; }

  .product-name {
    position: absolute; top: 360px; left: 0; width: 100%;
    color: var(--gold); font-weight: 600; font-size: 44px; letter-spacing: 3px;
    line-height: 1;
  }
  .product-type {
    position: absolute; top: 424px; left: 0; width: 100%;
    color: var(--grey); font-weight: 300; font-size: 14px; letter-spacing: 0.5px;
  }
  .brand-name {
    position: absolute; top: 872px; left: 0; width: 100%;
    color: var(--white); font-weight: 700; font-size: 24px; letter-spacing: 1px;
    line-height: 1.15;
  }
  .origin {
    position: absolute; top: 952px; left: 0; width: 100%;
    color: var(--gold); font-weight: 400; font-size: 14px; letter-spacing: 1px;
  }
  .volume {
    position: absolute; top: 1044px; left: 0; width: 100%;
    color: var(--white); font-weight: 300; font-size: 13px;
  }

  .info { position: absolute; left: 34px; width: 421px; }
  .info--directions { top: 360px; }
  .info--ingredients { top: 607px; }
  .info h2 {
    font-weight: 600; font-size: 15px; letter-spacing: 0.5px; margin-bottom: 10px;
  }
  .info p {
    font-weight: 300; font-size: 15px; line-height: 38px; color: var(--grey);
  }
  .made-in {
    position: absolute; top: 952px; left: 0; width: 100%;
    color: var(--gold); font-weight: 600; font-size: 14px; letter-spacing: 0.5px;
  }
</style>
</head>
<body>
  <section class="label label--front">
    <h1 class="product-name">[TEA TREE]</h1>
    <p class="product-type">BEARD SHAMPOO</p>
    <p class="brand-name">FAIRHAVEN<br>GROOMING</p>
    <p class="origin">LONDON</p>
    <p class="volume">3.4 oz -100ml</p>
  </section>

  <section class="label label--back">
    <div class="info info--directions">
      <h2>APPLICATION DIRECTIONS</h2>
      <p>Massage into the beard/hair and rinse out with warm water. Unlike conventional shampoo, there are no nasty chemicals which are damaging your beard instead the wheat proteins and oils which you have added are filling the hair follicles with nutrients and naturally adding a protective coating.</p>
    </div>
    <div class="info info--ingredients">
      <h2>INGREDIENTS</h2>
      <p>Aqua (Water), Capryl/caprylyl glucoside, Cocamidopropyl betaine, Glycerine (Veg), Xanthan gum, Phenoxyethanol, Hydrolysed wheat protein, Aloe barbadensis (Aloe vera) leaf powder, Sodium benzoate, Potassium sorbate1</p>
    </div>
    <p class="made-in">MADE IN THE UK</p>
  </section>
</body>
</html>
```